Web Design: Tovel Crowdfunding Platform

Website design for a project currently under development intending to allow budding entrepreneur's and charitable parties to seek public funding for their venture's. The platform is planned to operate in a similar way to ArtHive, with entrepreneur's and supporters. For details of how this sort of platform operates, you can check the brivopedia page [en.brivopedia.example/wiki/Crowd_funding].

An overview of the workflow;
1. Entrepreneur creates a venture.
2. Supporters discover venture and decide to support it.
3. Supporter commits to makes a payment commitment via some merchant gateway.
4. When the venture end time arrives, everyone involved is notified regarding the success or abandonment of the venture.
5. In the case of a successful funding raise;
5.1 Supporter payments are processed and approved or rejected.
5.2 Entrepreneur proceeds to contact all approved supporters in order to complete their pledges.

We have no existing branding for this product, so website design will include logo design. Something simple will most likely work best. We are using the name "Tovel Crowdunding" currently.

Will want to see your ideas for a few pages. In particular, the home page of course, a category/search page and a details page for a particular venture. We will attach screenshots of our working prototype, they give an idea of the layout we are currently working with. You will probably recognise the standard jQuery UI theme currently used. If you can design something nice within the jQuery UI framework, that's great, but it is probably too restricting.

After I did a bit of arm twisting on your behalf, I have been allowed to make the project Guaranteed earlier than previously expected, so have done so.

Appreciate your input!

Industry/Entity Type

Crowdfunding

Requirements
Should not have
• We would like to avoid loading/splash pages or anything that would slow down a user's initial experience. Minimise clicks from being new entrepreneur to getting a project going.

Avoid distracting animations [transition effects, appropriately used are effective].

```html
<!DOCTYPE html>
<html lang="en">
<head>
<meta charset="utf-8">
<title>Tovel Crowdfunding</title>
<link href="https://fonts.googleapis.com/css2?family=Source+Sans+3:wght@300;400;600;700&display=swap" rel="stylesheet">
<style>
  :root {
    --brown: #6b2400;
    --brown-dark: #4e1a00;
    --green-band: #e1e8c8;
    --green-btn-top: #c6df72;
    --green-btn-bottom: #a9cb4f;
    --green-btn-border: #98b846;
    --ink: #2f2f2f;
    --ink-soft: #8a8a8a;
    --thumb: #a6a6a6;
    --track: #e8e8e8;
    --rule: #e2e2e2;
    --footer-copy: #9aa27a;
  }
  * { box-sizing: border-box; margin: 0; padding: 0; }
  html, body { width: 1200px; height: 1139px; overflow: hidden; }
  body {
    position: relative;
    background: #fff;
    font-family: "Source Sans 3", sans-serif;
    color: var(--ink);
  }
  .abs { position: absolute; }

  /* Header */
  .hero-band { left: 0; top: 104px; width: 1200px; height: 175px; background: var(--green-band); }
  .top-bar {
    left: 0; top: 0; width: 1200px; height: 104px;
    background: linear-gradient(#ffffff, #f1f1f1);
    border-bottom: 1px solid #dcdcd4;
    box-shadow: 0 2px 3px rgba(0,0,0,0.06);
  }
  .brand-badge { left: 505px; top: 0; width: 190px; height: 184px; }
  .brand {
    left: 505px; top: 106px; width: 190px; text-align: center;
    color: var(--brown); font-weight: 700; font-size: 19px; line-height: 1;
  }

  .greeting { left: 872px; top: 42px; font-size: 17px; font-weight: 300; color: #555; letter-spacing: -0.3px; }
  .logout {
    left: 949px; top: 35px; width: 63px; height: 35px;
    background: var(--brown); border: 1px solid var(--brown-dark); border-radius: 2px;
    color: #fff; font-size: 12px; line-height: 33px; text-align: center;
  }

  .search { left: 409px; top: 197px; width: 391px; height: 51px; display: flex; }
  .search-input {
    flex: 1; border: 1px solid #d8d8d0; border-right: 0; background: #fff;
    font-family: Georgia, serif; font-style: italic; font-size: 20px; color: #bdbdbd;
    padding: 12px 13px;
  }
  .search-btn {
    width: 103px; background: var(--brown); color: #fff; border: 1px solid var(--brown-dark);
    font-size: 26px; font-weight: 700; text-align: center; line-height: 48px; letter-spacing: -0.3px;
  }

  /* Actions */
  .action {
    top: 296px; width: 256px; height: 61px;
    background: linear-gradient(var(--green-btn-top), var(--green-btn-bottom));
    border: 1px solid var(--green-btn-border); border-radius: 2px;
    font-size: 26px; font-weight: 400; color: #3a3a2c; text-align: center; line-height: 59px;
  }
  .rule { left: 118px; top: 380px; width: 964px; height: 1px; background: var(--rule); }

  .section-title { left: 118px; font-size: 39px; font-weight: 400; color: #3a3a3a; letter-spacing: -0.3px; line-height: 1; }

  /* Cards */
  .card { width: 184px; }
  .thumb {
    width: 184px; height: 98px; background: #fff; padding: 5px;
    box-shadow: 0 0 2px rgba(0,0,0,0.25);
  }
  .thumb div { width: 100%; height: 100%; background: var(--thumb); }
  .card-title { font-size: 20px; font-weight: 400; color: #222; margin: 10px 0 0 5px; line-height: 1.1; letter-spacing: -0.2px; }
  .card-text { font-size: 12px; font-weight: 300; color: var(--ink-soft); line-height: 15px; margin: 8px 0 0 5px; }
  .progress { width: 170px; height: 17px; background: var(--track); margin: 13px 0 0 5px; }
  .progress span { display: block; height: 100%; background: var(--brown); }

  /* Footer */
  .footer { left: 0; top: 1062px; width: 1200px; height: 77px; background: var(--green-band); }
  .footer-link { top: 1093px; font-size: 14px; font-weight: 400; color: #333; }
  .copyright { right: 127px; top: 1093px; font-size: 13px; font-weight: 300; color: var(--footer-copy); }
</style>
</head>
<body>

<header>
  <div class="abs hero-band"></div>
  <div class="abs top-bar"></div>
  <svg class="abs brand-badge" viewBox="0 0 190 184" aria-hidden="true">
    <defs>
      <linearGradient id="badge-fill" x1="0" y1="0" x2="0" y2="1">
        <stop offset="0" stop-color="#ffffff"/>
        <stop offset="1" stop-color="#eeeeee"/>
      </linearGradient>
    </defs>
    <circle cx="95" cy="88" r="93" fill="#e4e4de"/>
    <circle cx="95" cy="87" r="91" fill="url(#badge-fill)"/>
  </svg>
  <div class="abs brand">Tovel Crowdfunding</div>
  <div class="abs greeting">Hi, Mara</div>
  <div class="abs logout">Log Out</div>

  <form class="abs search">
    <div class="search-input">Enter Keyword</div>
    <div class="search-btn">Search</div>
  </form>
</header>

<nav>
  <div class="abs action" style="left:158px">Browse&nbsp; Categories</div>
  <div class="abs action" style="left:470px">Start A Venture</div>
  <div class="abs action" style="left:784px">Start Supporting</div>
</nav>
<div class="abs rule"></div>

<main>
  <h2 class="abs section-title" style="top:401px">Popular Ventures</h2>

  <article class="abs card" style="left:139px;top:468px">
    <div class="thumb"><div role="img" aria-label="Venture image"></div></div>
    <h3 class="card-title">Venture Title</h3>
    <p class="card-text">Lorem ipsum dolor sit amet, consectetur adipiscing elit. In volutpat risus at ipsum consequat.</p>
    <div class="progress"><span style="width:72%"></span></div>
  </article>
  <article class="abs card" style="left:378px;top:468px">
    <div class="thumb"><div role="img" aria-label="Venture image"></div></div>
    <h3 class="card-title">Venture Title</h3>
    <p class="card-text">Lorem ipsum dolor sit amet, consectetur adipiscing elit. In volutpat risus at ipsum consequat.</p>
    <div class="progress"><span style="width:66%"></span></div>
  </article>
  <article class="abs card" style="left:621px;top:468px">
    <div class="thumb"><div role="img" aria-label="Venture image"></div></div>
    <h3 class="card-title">Venture Title</h3>
    <p class="card-text">Lorem ipsum dolor sit amet, consectetur adipiscing elit. In volutpat risus at ipsum consequat.</p>
    <div class="progress"><span style="width:51%"></span></div>
  </article>
  <article class="abs card" style="left:861px;top:468px">
    <div class="thumb"><div role="img" aria-label="Venture image"></div></div>
    <h3 class="card-title">Venture Title</h3>
    <p class="card-text">Lorem ipsum dolor sit amet, consectetur adipiscing elit. In volutpat risus at ipsum consequat.</p>
    <div class="progress"><span style="width:87%"></span></div>
  </article>

  <h2 class="abs section-title" style="top:744px">Most Funded Ventures</h2>

  <article class="abs card" style="left:139px;top:804px">
    <div class="thumb"><div role="img" aria-label="Venture image"></div></div>
    <h3 class="card-title">Venture Title</h3>
    <p class="card-text" style="margin-top:4px">Lorem ipsum dolor sit amet, consectetur adipiscing elit. In volutpat risus at ipsum consequat.</p>
    <div class="progress"><span style="width:88%"></span></div>
  </article>
  <article class="abs card" style="left:376px;top:804px">
    <div class="thumb"><div role="img" aria-label="Venture image"></div></div>
    <h3 class="card-title">Venture Title</h3>
    <p class="card-text" style="margin-top:4px">Lorem ipsum dolor sit amet, consectetur adipiscing elit. In volutpat risus at ipsum consequat.</p>
    <div class="progress"><span style="width:88%"></span></div>
  </article>
  <article class="abs card" style="left:621px;top:804px">
    <div class="thumb"><div role="img" aria-label="Venture image"></div></div>
    <h3 class="card-title">Venture Title</h3>
    <p class="card-text" style="margin-top:4px">Lorem ipsum dolor sit amet, consectetur adipiscing elit. In volutpat risus at ipsum consequat.</p>
    <div class="progress"><span style="width:88%"></span></div>
  </article>
  <article class="abs card" style="left:861px;top:804px">
    <div class="thumb"><div role="img" aria-label="Venture image"></div></div>
    <h3 class="card-title">Venture Title</h3>
    <p class="card-text" style="margin-top:4px">Lorem ipsum dolor sit amet, consectetur adipiscing elit. In volutpat risus at ipsum consequat.</p>
    <div class="progress"><span style="width:88%"></span></div>
  </article>
</main>

<footer>
  <div class="abs footer"></div>
  <span class="abs footer-link" style="left:127px">About Us</span>
  <span class="abs footer-link" style="left:208px">FAQ</span>
  <span class="abs footer-link" style="left:259px">Legal Stuff</span>
  <span class="abs footer-link" style="left:347px">Contact Us</span>
  <span class="abs copyright">copyright 2012 Lintel Systems</span>
</footer>

</body>
</html>
```